Makers' Hollow - Landing page for small and large screen

Makers’ Hollow gives you the space you need to take your side project from idea to reality.

With three days of focused work, it’s a place for you iron out the details of your business idea away from the distractions of the city.

The full copy and structure is here:
https://www.makershollow-example.co.uk/landing

What it needs, a touch of colour.

Target Market(s)

25-35 working in digital industry, software developer, a UI or UX designer

Number of Pages Required

1 page

Font styles to use
Sans Serif

Colors
0292cd
33b8a4
86cfc6
fdf9cf
ec1f27

Requirements
Should not have
• gradients or too much images

```html
<!DOCTYPE html>
<html lang="en">
<head>
<meta charset="utf-8">
<title>Makers’ Hollow – focus. build. share.</title>
<link href="https://fonts.googleapis.com/css2?family=Raleway:wght@400;500;600&family=Roboto:wght@400;500;700&display=swap" rel="stylesheet">
<style>
:root{
  --blue:#1a84c8;
  --blue-bright:#0292cd;
  --teal:#33b8a4;
  --mint:#86cfc6;
  --red:#ec1f27;
  --ink:#222;
  --body:#3a3a3a;
  --grey-panel:#ebebeb;
  --footer:#0a0a0a;
  --white:#fff;
}
*{margin:0;padding:0;box-sizing:border-box}
html,body{width:1200px;height:3371px;overflow:hidden}
body{position:relative;background:var(--white);font-family:'Roboto',Arial,sans-serif;color:var(--body)}
.abs{position:absolute}

/* header + hero */
.hero{left:0;top:0;width:1200px;height:656px;background:linear-gradient(100deg,#3b3f44 0%,#6b6a66 35%,#8c8f92 60%,#4d5660 100%)}
.topbar{left:0;top:0;width:1200px;height:76px;background:rgba(20,20,20,.82);border-top:3px solid var(--blue-bright)}
.brand-name{color:var(--white);font-family:'Roboto',Arial,sans-serif;font-weight:500;font-size:27px;letter-spacing:-.3px;line-height:1}
.header-brand{left:85px;top:24px}
.nav{left:530px;top:24px;font-size:17px;color:var(--white)}
.nav a{color:var(--white);text-decoration:none;position:absolute;white-space:nowrap}
.nav a.active{color:var(--teal)}
.search{left:1084px;top:26px}
.hero-title{left:85px;top:283px;color:var(--white);font-family:'Raleway',Arial,sans-serif;font-weight:600;font-size:60px;line-height:1}
.hero-tag{left:85px;top:357px;color:var(--white);font-family:'Raleway',Arial,sans-serif;font-weight:600;font-size:36px}
.watch{left:85px;top:428px;display:flex;align-items:center;gap:14px;color:var(--white);font-size:17px;letter-spacing:.5px}

/* text sections */
.lead-heading{left:0;width:1200px;text-align:center;color:var(--blue);font-family:'Raleway',Arial,sans-serif;font-weight:500;font-size:32px;line-height:45px}
.lead-heading.focus{font-size:29.5px}
.lead-copy{left:94px;width:1012px;text-align:center;font-size:15.5px;line-height:31.5px;color:var(--body)}

/* join */
.join-photo{left:0;top:1094px;width:522px;height:438px;background:linear-gradient(160deg,#e6e4df 0%,#b9b7b1 45%,#6f7469 100%)}
.join-panel{left:524px;top:1094px;width:676px;height:438px;background:var(--grey-panel)}
.join-title{left:602px;top:1136px;font-family:'Raleway',Arial,sans-serif;font-weight:500;font-size:35px;color:var(--ink)}
.perks{left:607px;top:1200px;list-style:none}
.perks li{display:flex;align-items:center;gap:10px;height:32.3px;font-size:15.5px;color:#444}
.btn-join{left:609px;top:1451px;width:111px;height:30px;border-radius:15px;background:var(--red);color:var(--white);font-size:14px;font-weight:500;display:flex;align-items:center;justify-content:center;letter-spacing:.3px}

/* organisers */
.organisers{left:0;top:2027px;width:1200px;height:521px;background:linear-gradient(120deg,#0e3a63 0%,#0b2a4a 45%,#12406b 75%,#0a2440 100%)}
.org-title{left:0;top:2105px;width:1200px;text-align:center;color:var(--white);font-family:'Raleway',Arial,sans-serif;font-weight:500;font-size:45px}
.card{top:2222px;width:450px;height:223px;background:var(--white);border-radius:5px}
.avatar{width:126px;height:126px;border-radius:50%;border:5px solid var(--white);box-shadow:0 2px 8px rgba(0,0,0,.35)}
.card-copy{top:74px;left:110px;width:310px;font-size:15px;line-height:23px;color:#333;text-align:justify}
.quote{top:18px;right:34px}
.stars{top:159px;left:110px}
.card-name{top:158px;right:32px;font-size:18px;color:var(--blue)}

/* feedback */
.feedback{left:222px;top:2672px;width:756px;height:211px;border:2px solid var(--blue-bright)}
.fb-title{left:0;top:2708px;width:1200px;text-align:center;font-family:'Raleway',Arial,sans-serif;font-weight:500;font-size:35px;color:var(--ink)}
.fb-copy{left:0;top:2766px;width:1200px;text-align:center;font-size:18px;line-height:34px;color:#333}
.btn-share{left:488px;top:2861px;width:224px;height:47px;background:var(--teal);color:var(--white);font-size:17px;font-weight:500;display:flex;align-items:center;justify-content:center;box-shadow:0 2px 4px rgba(0,0,0,.2)}

/* footer */
.footer{left:0;top:3002px;width:1200px;height:369px;background:var(--footer)}
.footer-brand{left:85px;top:3130px}
.social{left:96px;top:3204px;display:flex;gap:13px}
.social span{width:28px;height:28px;border-radius:50%;border:1.5px solid var(--white);display:block}
.foot-head{top:3064px;color:var(--white);font-size:20px;font-weight:500}
.foot-links{left:362px;top:3119px;list-style:none;color:var(--white);font-size:13px}
.foot-links li{height:23px;display:flex;align-items:center;gap:7px}
.contact-row{left:517px;display:flex;gap:14px;color:var(--white);font-size:13px;line-height:22px}
.field{left:809px;width:281px;height:35px;background:var(--white);font-size:12px;color:#666;padding-left:14px;display:flex;align-items:center}
.btn-signup{left:809px;top:3211px;width:122px;height:35px;background:var(--red);color:var(--white);font-size:14px;display:flex;align-items:center;justify-content:center}
.copyright{left:0;top:3328px;width:1200px;text-align:center;color:#bbb;font-size:15px}
</style>
</head>
<body>

<!-- header / hero -->
<div class="abs hero" role="img" aria-label="Photo of smiling creatives working together at a desk"></div>
<div class="abs topbar"></div>
<div class="abs brand-name header-brand">Makers’ Hollow</div>
<nav class="abs nav">
  <a class="active" style="left:0">Home</a>
  <a style="left:106px">About us</a>
  <a style="left:232px">Service</a>
  <a style="left:351px">Blog</a>
  <a style="left:449px">Contact</a>
</nav>
<svg class="abs search" width="22" height="22" viewBox="0 0 22 22"><circle cx="9" cy="9" r="6.5" fill="none" stroke="#fff" stroke-width="3"/><line x1="14" y1="14" x2="20" y2="20" stroke="#fff" stroke-width="3.5" stroke-linecap="round"/></svg>

<h1 class="abs hero-title">Makers’ Hollow</h1>
<div class="abs hero-tag">focus. build. share.</div>
<div class="abs watch">
  <svg width="30" height="30" viewBox="0 0 30 30"><circle cx="15" cy="15" r="15" fill="var(--red)"/><polygon points="12,9 21,15 12,21" fill="#fff"/></svg>
  <span>WATCH VIDEO</span>
</div>

<!-- intro -->
<h2 class="abs lead-heading" style="top:748px">Makers’ Hollow gives you the space you need to take<br>your side project from idea to reality</h2>
<p class="abs lead-copy" style="top:861px">Calling all creatives! Whether you’re a software developer, a UI or UX designer, a product creator or an artworker, you’ll know only too well that great work rarely materialises when you’re in the wrong environment. Phones buzzing. Emails pinging. Video calls incoming...distractions are everywhere – and they do nothing for your motivation. So, if you have a seed of a business idea and need to reclaim some focus, the Makers’ Hollow is for you. Or maybe you’ve created a product, sought a patent and you’re ready – and raring – to go.</p>

<!-- join -->
<div class="abs join-photo" role="img" aria-label="Photo of a bright open-plan office with desks and bookshelves"></div>
<div class="abs join-panel"></div>
<h2 class="abs join-title">Join the Hollow and enjoy</h2>
<ul class="abs perks">
  <li><svg width="14" height="14" viewBox="0 0 14 14"><circle cx="7" cy="7" r="7" fill="var(--teal)"/><path d="M4 7.2l2 2 4-4.2" fill="none" stroke="#fff" stroke-width="1.8"/></svg>Three, full days of distraction-free work</li>
  <li><svg width="14" height="14" viewBox="0 0 14 14"><circle cx="7" cy="7" r="7" fill="var(--teal)"/><path d="M4 7.2l2 2 4-4.2" fill="none" stroke="#fff" stroke-width="1.8"/></svg>A chance to hone your side project away from the office</li>
  <li><svg width="14" height="14" viewBox="0 0 14 14"><circle cx="7" cy="7" r="7" fill="var(--teal)"/><path d="M4 7.2l2 2 4-4.2" fill="none" stroke="#fff" stroke-width="1.8"/></svg>The opportunity to collaborate with likeminded creatives</li>
  <li><svg width="14" height="14" viewBox="0 0 14 14"><circle cx="7" cy="7" r="7" fill="var(--teal)"/><path d="M4 7.2l2 2 4-4.2" fill="none" stroke="#fff" stroke-width="1.8"/></svg>Good, honest feedback and insight from fellow attendees</li>
  <li><svg width="14" height="14" viewBox="0 0 14 14"><circle cx="7" cy="7" r="7" fill="var(--teal)"/><path d="M4 7.2l2 2 4-4.2" fill="none" stroke="#fff" stroke-width="1.8"/></svg>Daily yoga and meditation to help fuel your ideas</li>
  <li><svg width="14" height="14" viewBox="0 0 14 14"><circle cx="7" cy="7" r="7" fill="var(--teal)"/><path d="M4 7.2l2 2 4-4.2" fill="none" stroke="#fff" stroke-width="1.8"/></svg>Three, nutritious and delicious meals a day</li>
  <li><svg width="14" height="14" viewBox="0 0 14 14"><circle cx="7" cy="7" r="7" fill="var(--teal)"/><path d="M4 7.2l2 2 4-4.2" fill="none" stroke="#fff" stroke-width="1.8"/></svg>Healthy, low-sugar snacks to get you through the day</li>
</ul>
<div class="abs btn-join">JOIN NOW</div>

<!-- focus -->
<h2 class="abs lead-heading focus" style="top:1665px">With three days of focused work, it’s a place for you iron out the details<br>of your business idea away from the distractions of the city.</h2>
<p class="abs lead-copy" style="top:1771px">Whatever stage your side hustle’s at, we’re here to help it thrive. Our warm and friendly Hollow is just that: a place to create, connect and collaborate with likeminded folks. Oh, and there’s yoga, meditation, healthy meals and snacks, and all the feedback you need to power on through.And while you’re busy getting your side project off the ground, we’ll rustle up three healthy meals each day so that you don’t have to worry about cooking. We’ll even make sure you have a steady supply of healthy, low-sugar snacks to help fuel all those bright ideas.</p>

<!-- organisers -->
<div class="abs organisers" role="img" aria-label="Dark navy faceted background pattern"></div>
<h2 class="abs org-title">Meet Your Hollow Organisers</h2>

<div class="abs card" style="left:130px">
  <svg class="abs quote" width="50" height="36" viewBox="0 0 50 36"><path d="M2 36V20C2 8 8 2 20 0v7c-6 2-8 6-8 11h8v18zM28 36V20C28 8 34 2 46 0v7c-6 2-8 6-8 11h8v18z" fill="var(--blue)"/></svg>
  <p class="abs card-copy">A software engineer in London, Tomas knows only too well the challenges faced by creatives; it’s the reason he’s organised the</p>
  <svg class="abs stars" width="70" height="14" viewBox="0 0 70 14"><g fill="#f2a516"><polygon points="7,0 9,5 14,5 10,8.5 11.5,14 7,10.8 2.5,14 4,8.5 0,5 5,5"/><polygon transform="translate(15)" points="7,0 9,5 14,5 10,8.5 11.5,14 7,10.8 2.5,14 4,8.5 0,5 5,5"/><polygon transform="translate(30)" points="7,0 9,5 14,5 10,8.5 11.5,14 7,10.8 2.5,14 4,8.5 0,5 5,5"/><polygon transform="translate(45)" points="7,0 9,5 14,5 10,8.5 11.5,14 7,10.8 2.5,14 4,8.5 0,5 5,5"/><polygon transform="translate(60)" points="7,0 7,10.8 2.5,14 4,8.5 0,5 5,5"/></g></svg>
  <div class="abs card-name">Tomas Ferrin</div>
</div>
<div class="abs avatar" style="left:90px;top:2274px;background:#5d5b57" role="img" aria-label="Portrait photo of organiser Tomas Ferrin"></div>

<div class="abs card" style="left:652px">
  <svg class="abs quote" width="50" height="36" viewBox="0 0 50 36"><path d="M2 36V20C2 8 8 2 20 0v7c-6 2-8 6-8 11h8v18zM28 36V20C28 8 34 2 46 0v7c-6 2-8 6-8 11h8v18z" fill="var(--blue)"/></svg>
  <p class="abs card-copy">An internationally-certified yoga teacher, Lia loves connecting with people and discovering how she can help them get</p>
  <svg class="abs stars" width="70" height="14" viewBox="0 0 70 14"><g fill="#f2a516"><polygon points="7,0 9,5 14,5 10,8.5 11.5,14 7,10.8 2.5,14 4,8.5 0,5 5,5"/><polygon transform="translate(15)" points="7,0 9,5 14,5 10,8.5 11.5,14 7,10.8 2.5,14 4,8.5 0,5 5,5"/><polygon transform="translate(30)" points="7,0 9,5 14,5 10,8.5 11.5,14 7,10.8 2.5,14 4,8.5 0,5 5,5"/><polygon transform="translate(45)" points="7,0 9,5 14,5 10,8.5 11.5,14 7,10.8 2.5,14 4,8.5 0,5 5,5"/><polygon transform="translate(60)" points="7,0 7,10.8 2.5,14 4,8.5 0,5 5,5"/></g></svg>
  <div class="abs card-name">Lia Marsden</div>
</div>
<div class="abs avatar" style="left:612px;top:2274px;background:#b39a52" role="img" aria-label="Portrait photo of organiser Lia Marsden"></div>

<!-- feedback -->
<div class="abs feedback"></div>
<h2 class="abs fb-title">What do you think?</h2>
<p class="abs fb-copy">Sound good? Keen to know more? Share some feedback via the<br>button below and we can hone the Hollow to suit you.</p>
<div class="abs btn-share">Share your thoughts...</div>

<!-- footer -->
<footer class="abs footer"></footer>
<div class="abs brand-name footer-brand">Makers’ Hollow</div>
<div class="abs social"><span></span><span></span><span></span><span></span></div>

<div class="abs foot-head" style="left:362px">Links</div>
<ul class="abs foot-links">
  <li>» Home</li><li>» About us</li><li>» Service</li><li>» News</li><li>» Join Us</li>
</ul>

<div class="abs foot-head" style="left:517px">Contact Us</div>
<div class="abs contact-row" style="top:3112px">
  <svg width="13" height="18" viewBox="0 0 13 18" style="margin-top:4px"><path d="M6.5 0A6.5 6.5 0 0 0 0 6.5C0 11 6.5 18 6.5 18S13 11 13 6.5A6.5 6.5 0 0 0 6.5 0z" fill="#fff"/><circle cx="6.5" cy="6.5" r="2.5" fill="#0a0a0a"/></svg>
  <span>218 Alder Row Suite<br>#40 Fairview, ST 00000</span>
</div>
<div class="abs contact-row" style="top:3175px">
  <svg width="14" height="14" viewBox="0 0 14 14" style="margin-top:4px"><path d="M3 0l3 3-2 2c1 2 3 4 5 5l2-2 3 3-2 3C6 14 0 8 0 3z" fill="#fff"/></svg>
  <span>+1 800 555 0142</span>
</div>
<div class="abs contact-row" style="top:3216px">
  <svg width="14" height="11" viewBox="0 0 14 11" style="margin-top:6px"><rect width="14" height="11" fill="#fff"/><path d="M0 0l7 6 7-6" fill="none" stroke="#0a0a0a" stroke-width="1.3"/></svg>
  <span>hello@makershollow-example.co.uk</span>
</div>

<div class="abs foot-head" style="left:809px">Newsletter sign up</div>
<div class="abs field" style="top:3121px">Enter email</div>
<div class="abs field" style="top:3162px">Zip</div>
<div class="abs btn-signup">JOIN US</div>

<div class="abs copyright">© 2019 Company Name &nbsp;All right reserved</div>

</body>
</html>
```